Rapidly growing regional logistics company looking for a modern clean website design.

We need a website for a 5 year old company based in New England.
We offer a complete logistics solution. With services dedicated to the changing economic environment. Services to our customers include, same day delivery, trucking and van service, warehouse & storage, pool distribution, and B2B installations.
We've implemented leading technology along the way, that provides visibility, accountability, up to the minute tracking, and project management.
Our goal to be known in the industry we service as an excellent provider of time-critical services and dependability.
Independently of the services we offer, our customers know that they can count on a true partner.

Target Market(s)

B2B, including printers, retail, manufacturers, wholesalers, electronics, any company that needs product delivered or warehoused

Industry/Entity Type

Logistics

Coding

Coded - Design and coding required

Number of Pages Required

5+ page

Font styles to use
Sans Serif

Colors
0255a3

Requirements
Must have
• Clean, modern design, limited clutter. Limited tabs, preferred everything on 1st screen roll down to see info

```html
<!DOCTYPE html>
<html lang="en">
<head>
<meta charset="utf-8">
<title>Harborline Logistics</title>
<link href="https://fonts.googleapis.com/css2?family=Montserrat:wght@300;400;500;600&display=swap" rel="stylesheet">
<style>
:root{
  --blue:#3d64b0;
  --blue-deep:#0255a3;
  --ink:#2b2b2b;
  --muted:#6a6a6a;
  --line:#d8d8d8;
  --white:#ffffff;
  --grey-icon:#b5b5b5;
}
*{margin:0;padding:0;box-sizing:border-box}
html,body{width:1200px;height:2253px;overflow:hidden;background:var(--white)}
body{font-family:'Montserrat',sans-serif;color:var(--ink);position:relative}
.abs{position:absolute}
a{color:inherit;text-decoration:none}

/* header */
.site-header{position:absolute;left:0;top:0;width:1200px;height:97px;background:var(--white)}
.brand{left:135px;top:30px;display:flex;align-items:center;gap:10px}
.brand-dot{width:34px;height:34px;border-radius:50%;background:var(--blue)}
.brand-name{font-size:17px;font-weight:500;color:var(--blue);letter-spacing:.5px;line-height:1.1}
.main-nav{left:404px;top:43px;display:flex;gap:28px;font-size:11px;letter-spacing:.6px;color:var(--ink)}
.main-nav .active{color:var(--blue)}
.call{left:760px;top:43px;font-size:11px;font-weight:500;letter-spacing:.3px}
.quote-btn{left:902px;top:35px;width:155px;height:29px;border-radius:15px;background:var(--blue);color:var(--white);font-size:10px;letter-spacing:.6px;display:flex;align-items:center;justify-content:center;box-shadow:0 1px 0 #23418a}

/* hero */
.hero{left:0;top:97px;width:1200px;height:390px;background:linear-gradient(110deg,#5b6470 0%,#8d9299 35%,#c9ccd0 55%,#6f7780 75%,#254c86 100%)}
.hero-copy{left:207px;top:215px;color:var(--white)}
.hero-copy h1{font-size:25px;font-weight:300;line-height:1.1}
.hero-copy h1 strong{display:block;font-size:21px;font-weight:500;margin-top:2px}
.hero-copy p{font-size:12px;line-height:1.3;margin-top:10px;width:270px}
.ghost-btn{display:flex;align-items:center;justify-content:center;gap:14px;height:30px;border:1px solid var(--white);border-radius:15px;color:var(--white);font-size:10px;letter-spacing:.6px}
.hero .ghost-btn{position:absolute}
.hero-arrow{top:262px}

/* services */
.section-title{left:0;width:1200px;top:545px;text-align:center;color:var(--blue);font-size:21px;font-weight:500;letter-spacing:.8px}
.service-card{top:592px;width:248px}
.service-card .media{height:142px}
.service-card h3{margin-top:26px;font-size:13px;font-weight:500;letter-spacing:.8px;display:inline-block;border-bottom:1px solid var(--ink);padding-bottom:1px}
.service-card p{margin-top:14px;font-size:10px;line-height:1.45;color:var(--muted);width:245px}
.outline-btn{position:absolute;display:flex;align-items:center;justify-content:center;gap:18px;width:106px;height:30px;border:1px solid var(--blue);border-radius:15px;color:var(--blue);font-size:10px;letter-spacing:.6px;background:var(--white)}
.outline-btn.filled{background:var(--blue);color:var(--white);box-shadow:0 1px 0 #23418a}

/* feature bands */
.band{left:0;width:1200px;height:352px}
.band-driver{top:951px;background:linear-gradient(90deg,#b8bcc0 0%,#d3d2cc 30%,#8a8680 55%,#5a5f66 70%,#a32a30 88%,#c8333a 100%)}
.band-courier{top:1611px;background:linear-gradient(90deg,#b07a4a 0%,#d3a274 25%,#7c838c 45%,#9fb6d2 60%,#3f6db0 85%,#204f92 100%)}
.callout{width:382px}
.callout-head{height:106px;background:var(--blue);color:var(--white);padding:38px 36px 0;font-size:19px;font-weight:500;letter-spacing:.5px;line-height:1.2;border-radius:10px 10px 0 0}
.callout-body{height:105px;background:var(--white);padding:20px 36px;font-size:10px;line-height:1.45;color:var(--muted);border-radius:14px 0 14px 14px;margin-top:-6px;position:relative}
.callout .ghost-btn{width:133px;margin-left:36px;margin-top:0}

/* delivery features */
.feature{top:1370px;width:380px}
.feature-icon{position:absolute;left:0;top:4px}
.feature h3{margin-left:68px;font-size:13px;font-weight:500;letter-spacing:.8px;line-height:1.35;display:inline-block;border-bottom:1px solid var(--ink);width:160px}
.feature p{margin-left:68px;margin-top:14px;font-size:10px;line-height:1.5;color:var(--muted);width:310px}

/* footer */
.site-footer{left:0;top:1963px;width:1200px;height:290px;background:var(--white)}
.foot-col h4{font-size:10px;font-weight:600;color:var(--blue);letter-spacing:.8px}
.foot-col p{font-size:10px;color:var(--muted);line-height:1.45}
.foot-col .lead{font-size:13px;color:var(--ink);margin-top:14px}
.quick-links{list-style:none;margin-top:18px;font-size:10px;line-height:1.85;color:var(--muted)}
.quick-links .current{color:var(--blue);text-decoration:underline}
.copyright{font-size:10px;color:var(--blue);letter-spacing:.6px;line-height:1.5}
.copyright span{letter-spacing:0}
.socials{display:flex;gap:8px;margin-top:22px}
.socials i{width:21px;height:21px;border-radius:50%;background:var(--grey-icon);display:block}
</style>
</head>
<body>

<header class="site-header">
  <div class="brand abs"><span class="brand-dot"></span><span class="brand-name">HARBORLINE<br>LOGISTICS</span></div>
  <nav class="main-nav abs">
    <a class="active">HOME</a><a>ABOUT US</a><a>SERVICES</a><a>CONTACT US</a>
  </nav>
  <div class="call abs">CALL US: +100 555 0142</div>
  <a class="quote-btn abs">REQUEST A QUOTE</a>
</header>

<section class="hero abs" role="img" aria-label="Photo of a white truck with blue trailer driving on a highway">
  <div class="hero-copy abs" style="top:118px">
    <h1>We offer a complete<strong>logistics solution in New England</strong></h1>
    <p>With services dedicated to the changing economic environment.</p>
  </div>
  <a class="ghost-btn" style="left:207px;top:240px;width:142px">CONTACT US <span>&rarr;</span></a>
  <svg class="abs hero-arrow" style="left:50px;top:170px" width="26" height="54" viewBox="0 0 26 54"><path d="M24 2 L2 27 L24 52" fill="none" stroke="#fff" stroke-width="2"/></svg>
  <svg class="abs hero-arrow" style="left:1124px;top:170px" width="26" height="54" viewBox="0 0 26 54"><path d="M2 2 L24 27 L2 52" fill="none" stroke="#fff" stroke-width="2"/></svg>
</section>

<h2 class="section-title abs">TRANSPORT &amp; LOGISTICS SERVICE</h2>

<article class="service-card abs" style="left:207px">
  <div class="media" role="img" aria-label="Photo of a modern warehouse building under a blue sky" style="background:linear-gradient(160deg,#7fb4e6,#c9d9e6 55%,#8a8e94)"></div>
  <h3>WAREHOUSING</h3>
  <p>Our warehouse facility may prove to be one of the most valuable extensions of your company's operations.</p>
</article>
<a class="outline-btn" style="left:201px;top:851px">MORE <span>&rarr;</span></a>

<article class="service-card abs" style="left:476px">
  <div class="media" role="img" aria-label="Photo of a truck with blue trailer on the road" style="background:linear-gradient(160deg,#9aa6b4,#dfe3e8 45%,#3a6bb4)"></div>
  <h3>TRUCK &amp; VAN</h3>
  <p>we are open 24 hours per day, 365 days per year with Trucking, vehicle and ground transportation Service.</p>
</article>
<a class="outline-btn filled" style="left:476px;top:851px">MORE <span>&rarr;</span></a>

<article class="service-card abs" style="left:744px">
  <div class="media" role="img" aria-label="Photo of cardboard boxes on a conveyor belt" style="background:linear-gradient(160deg,#e8e2da,#c79a64 50%,#a8815a)"></div>
  <h3>DISTRIBUTION &amp; POOL</h3>
  <p>Our highly superior and cost-effective alternative to the higher cost of LTL shipments Service.</p>
</article>
<a class="outline-btn" style="left:744px;top:851px">MORE <span>&rarr;</span></a>

<section class="band band-driver abs" role="img" aria-label="Photo of a truck driver in sunglasses and cap at the wheel of a red cab">
  <div class="callout abs" style="left:207px;top:56px">
    <div class="callout-head">NO JOB IS TOO BIG<br>FOR US.</div>
    <div class="callout-body">Our goal to be known in the industry we service as an excellent provider of time-critical services and dependability.</div>
    <a class="ghost-btn" style="margin-left:43px;width:133px">ABOUT US <span>&rarr;</span></a>
  </div>
</section>

<article class="feature abs" style="left:207px">
  <svg class="feature-icon" width="36" height="52" viewBox="0 0 36 52"><path d="M6 4 L10 4 L14 40 L34 40" fill="none" stroke="var(--blue)" stroke-width="3"/><rect x="14" y="14" width="18" height="22" fill="var(--blue)"/><path d="M23 31 V20 M18 25 L23 20 L28 25" fill="none" stroke="#fff" stroke-width="2"/><circle cx="16" cy="46" r="4" fill="var(--blue)"/><circle cx="30" cy="46" r="4" fill="var(--blue)"/></svg>
  <h3>SAME-DAY DELIVERY SERVICE</h3>
  <p>Regardless of the specifics of your needs, HARBORLINE can handle your same-day delivery needs. Harborline Logistics offers same-day delivery services as a standalone service or in support of our other services.</p>
</article>
<a class="outline-btn" style="left:275px;top:1511px">MORE <span>&rarr;</span></a>

<article class="feature abs" style="left:609px">
  <svg class="feature-icon" width="48" height="52" viewBox="0 0 48 52"><rect x="10" y="2" width="28" height="10" rx="3" fill="var(--blue)"/><rect x="6" y="12" width="36" height="26" rx="2" fill="var(--blue)"/><rect x="11" y="16" width="26" height="9" fill="#fff"/><rect x="2" y="38" width="44" height="6" fill="var(--blue)"/><rect x="6" y="44" width="8" height="7" fill="var(--blue)"/><rect x="34" y="44" width="8" height="7" fill="var(--blue)"/></svg>
  <h3>DEDICATED DELIVERY SERVICE</h3>
  <p>Our goal is to make the process easy, and of course, to make you look good in the eyes of your customers and suppliers.Whether your needs are a car to tractor trailer Harborline can provide the solution for you.</p>
</article>
<a class="outline-btn" style="left:677px;top:1511px">MORE <span>&rarr;</span></a>

<section class="band band-courier abs" role="img" aria-label="Photo of a smiling courier carrying cardboard boxes and a clipboard beside a delivery van">
  <div class="callout abs" style="left:610px;top:56px">
    <div class="callout-head">FOR ANY HELP OR<br>QUERIES</div>
    <div class="callout-body"><span style="font-size:14px;color:var(--ink)">Call Now: +100 555 0142 / +100 555 0142</span><br>or you can also Email Us</div>
    <a class="ghost-btn" style="width:141px">CONTACT US <span>&rarr;</span></a>
  </div>
</section>

<footer class="site-footer abs">
  <div class="foot-col abs" style="left:207px;top:72px">
    <h4>CONTACT US</h4>
    <p class="lead">Call Us: +100 555 0142 / +100 555 0142</p>
    <p>info@harborlinelogistics.com</p>
    <p style="margin-top:18px">Harborline Logistics<br>48 Quarry Lane&nbsp; Millbrook,<br>NL&nbsp; B2C 4D5</p>
  </div>
  <div class="foot-col abs" style="left:542px;top:72px">
    <h4>QUICK LINK</h4>
    <ul class="quick-links">
      <li class="current">Our Company</li><li>Services</li><li>Request For Quote</li><li>Terms &amp; Conditions</li><li>Privacy Policy</li><li>Contact</li>
    </ul>
  </div>
  <div class="foot-col abs" style="left:744px;top:70px">
    <p class="copyright">&copy; 2017 HARBORLINE LOGISTICS.<br><span>All right reserved.</span></p>
    <div class="socials"><i></i><i></i><i></i><i></i></div>
  </div>
  <svg class="abs" style="left:1024px;top:72px" width="22" height="14" viewBox="0 0 22 14"><path d="M11 0 L22 14 L0 14 Z" fill="var(--blue)"/></svg>
</footer>

</body>
</html>
```